Identity Package (Logo, Website)

We need a logo and website design for a new company.
The new company is a voicemail transcription service provider. It's name is KB7LUX.io
It will be very transactional. We like the "bootstrap" look and feel, and will be using a developer familiar with bootstrap. Here are the kinds of webpages we like :
https://www.plinverotrack.io
http://www.quorvix.com/
http://www.brenmoda.com/
There will only be 5 pages, as follows :
1- Homepage
2- Voicemail Transcription for Individuals
3- Voicemail Transcription for Companies
4- Wholesale Voicemail Transcription for Service Providers/Enterprises
5- Contact us
As far as the logo is concerned, we'd like to have just stylized text. It should be done in such a way as to make it easy to see the different elements of the name, which are KB, 7, and LUX.
Reason: I have received a number of designs, but the designs are mostly from the same few designers (not that much variety in designers). I'd like a few more to compare if possible, so I thought I would keep this open until Monday to give more designers the opportunity to submit over the weekend. Thanks!

```html
<!DOCTYPE html>
<html lang="en">
<head>
<meta charset="utf-8">
<title>KB7LUX.io – Voice Mail Transcription To Text</title>
<link rel="stylesheet" href="https://fonts.googleapis.com/css2?family=Source+Sans+3:wght@400;600&family=Arimo:wght@700&family=Questrial&display=swap">
<style>
  :root {
    --topbar: #474646;
    --white: #ffffff;
    --nav-text: #333333;
    --hero: #0090d8;
    --button: #0a4a7a;
    --heading-blue: #0d4a7a;
    --tile-bright: #0090d8;
    --tile-muted: #3476b4;
    --body-text: #555555;
    --footer: #222222;
    --footer-accent: #1a94d6;
    --bottombar: #050505;
    --bottom-text: #b5b5b5;
    --social: #2f5ea0;
  }
  * { margin: 0; padding: 0; box-sizing: border-box; }
  html, body { width: 1200px; height: 1138px; overflow: hidden; }
  body { position: relative; background: var(--white); font-family: "Source Sans 3", "Myriad Pro", sans-serif; }

  .topbar { position: absolute; left: 0; top: 0; width: 1200px; height: 52px; background: var(--topbar); }
  .brand { position: absolute; display: flex; align-items: center; gap: 8px; font-family: "Source Sans 3", sans-serif; font-weight: 600; color: var(--white); }
  .brand-square { width: 16px; height: 16px; background: var(--hero); }
  .topbar .brand { left: 91px; top: 6px; height: 40px; font-size: 31px; }

  .main-nav { position: absolute; left: 0; top: 52px; width: 1200px; height: 61px; }
  .main-nav a, .bottom-nav a { position: absolute; transform: translateX(-50%); text-decoration: none; white-space: nowrap; }
  .main-nav a { top: 11px; font-size: 18px; color: var(--nav-text); }

  .hero { position: absolute; left: 0; top: 113px; width: 1200px; height: 353px; background: var(--hero); }
  .hero-title { position: absolute; left: 133px; top: 47px; font-family: "Arimo", Helvetica, sans-serif; font-weight: 700; font-size: 30px; color: var(--white); white-space: nowrap; }
  .hero-text { position: absolute; left: 134px; top: 103px; width: 420px; font-size: 20px; line-height: 25px; color: var(--white); white-space: nowrap; }
  .hero-button { position: absolute; left: 133px; top: 193px; width: 164px; height: 50px; background: var(--button); color: var(--white); font-size: 18px; line-height: 50px; text-align: center; text-decoration: none; }
  .hero-visual { position: absolute; left: 648px; top: 31px; width: 442px; height: 277px; }
  .slider-dots { position: absolute; left: 527px; top: 316px; display: flex; gap: 17px; }
  .slider-dots span { width: 14px; height: 14px; border-radius: 50%; background: #7ccaf0; }
  .slider-dots span.active { background: var(--white); }

  .features { position: absolute; left: 0; top: 466px; width: 1200px; height: 357px; }
  .feature { position: absolute; top: 46px; width: 180px; transform: translateX(-50%); text-align: center; }
  .feature h3 { font-weight: 400; font-size: 20px; color: var(--heading-blue); height: 25px; }
  .feature-tile { width: 146px; height: 108px; margin: 10px auto 0; border-radius: 10px; }
  .feature-tile.bright { background: var(--tile-bright); }
  .feature-tile.muted { background: var(--tile-muted); }
  .feature p { width: 150px; margin: 20px auto 0; text-align: left; font-size: 13.5px; line-height: 17.5px; color: var(--body-text); white-space: nowrap; }

  .archive { position: absolute; left: 0; top: 823px; width: 1200px; height: 266px; background: var(--footer); font-family: "Questrial", "Century Gothic", sans-serif; }
  .archive-col { position: absolute; top: 34px; }
  .archive-col h4 { font-weight: 400; font-size: 33px; color: var(--footer-accent); height: 50px; }
  .archive-col a { display: block; height: 37px; padding-top: 8px; font-size: 17.5px; color: var(--white); text-decoration: none; }

  .bottombar { position: absolute; left: 0; top: 1089px; width: 1200px; height: 49px; background: var(--bottombar); }
  .bottombar .brand { left: 121px; top: 6px; height: 37px; font-size: 27px; color: var(--bottom-text); }
  .bottombar .brand-square { background: #8c8c8c; }
  .bottom-nav a { top: 12px; font-size: 18px; color: var(--bottom-text); }
  .social { position: absolute; top: 11px; left: 995px; display: flex; gap: 9px; }
  .social span { width: 26px; height: 26px; background: var(--social); }
</style>
</head>
<body>
  <header class="topbar">
    <div class="brand"><span class="brand-square"></span>KB7LUX.io</div>
  </header>

  <nav class="main-nav">
    <a href="#" style="left:337px">Home</a>
    <a href="#" style="left:453px">About</a>
    <a href="#" style="left:597px">Transcription</a>
    <a href="#" style="left:734px">FAQ</a>
    <a href="#" style="left:852px">Contact</a>
  </nav>

  <section class="hero">
    <h1 class="hero-title">Voice Mail Transcription To Text</h1>
    <p class="hero-text">Lorem Ipsum dolor sit amet consectetur adipis<br>ing elit et consectetur un lorem ipsum dolor sit<br>amet quore consectis.</p>
    <a class="hero-button" href="#">VIEW MORE</a>
    <svg class="hero-visual" role="img" aria-label="Two open laptops showing colourful desktop screens" viewBox="0 0 442 277">
      <defs>
        <linearGradient id="deviceTone" x1="0" y1="0" x2="1" y2="1">
          <stop offset="0" stop-color="#2a3a52"/>
          <stop offset="0.5" stop-color="#1f6fae"/>
          <stop offset="1" stop-color="#2b2f3a"/>
        </linearGradient>
      </defs>
      <rect x="0" y="0" width="442" height="277" rx="6" fill="url(#deviceTone)" opacity="0.55"/>
    </svg>
    <div class="slider-dots"><span class="active"></span><span></span><span></span><span></span><span></span></div>
  </section>

  <section class="features">
    <div class="feature" style="left:225px"><h3>Lorem Ipsum</h3><div class="feature-tile bright"></div><p>Lorem Ipsum dolor sit<br>amet consectetur adipis<br>ing elit et consectetur<br>un lorem ipsum dolor sit<br>amet quore consectis.</p></div>
    <div class="feature" style="left:410px"><h3>Lorem Ipsum</h3><div class="feature-tile muted"></div><p>Lorem Ipsum dolor sit<br>amet consectetur adipis<br>ing elit et consectetur<br>un lorem ipsum dolor sit<br>amet quore consectis.</p></div>
    <div class="feature" style="left:596px"><h3>Lorem Ipsum</h3><div class="feature-tile bright"></div><p>Lorem Ipsum dolor sit<br>amet consectetur adipis<br>ing elit et consectetur<br>un lorem ipsum dolor sit<br>amet quore consectis.</p></div>
    <div class="feature" style="left:781px"><h3>Lorem Ipsum</h3><div class="feature-tile muted"></div><p>Lorem Ipsum dolor sit<br>amet consectetur adipis<br>ing elit et consectetur<br>un lorem ipsum dolor sit<br>amet quore consectis.</p></div>
    <div class="feature" style="left:967px"><h3>Lorem Ipsum</h3><div class="feature-tile bright"></div><p>Lorem Ipsum dolor sit<br>amet consectetur adipis<br>ing elit et consectetur<br>un lorem ipsum dolor sit<br>amet quore consectis.</p></div>
  </section>

  <section class="archive">
    <div class="archive-col" style="left:160px"><h4>December</h4><a href="#">link one goes here</a><a href="#">link two goes here</a><a href="#">link one goes here</a></div>
    <div class="archive-col" style="left:407px"><h4>November</h4><a href="#">link one goes here</a><a href="#">link one goes here</a></div>
    <div class="archive-col" style="left:655px"><h4>October</h4><a href="#">link one goes here</a><a href="#">link two goes here</a><a href="#">link one goes here</a><a href="#">link two goes here</a></div>
    <div class="archive-col" style="left:892px"><h4>September</h4><a href="#">link one goes here</a><a href="#">link two goes here</a><a href="#">link one goes here</a></div>
  </section>

  <footer class="bottombar">
    <div class="brand"><span class="brand-square"></span>KB7LUX.io</div>
    <nav class="bottom-nav">
      <a href="#" style="left:350px">Home</a>
      <a href="#" style="left:465px">About</a>
      <a href="#" style="left:609px">Transcription</a>
      <a href="#" style="left:746px">FAQ</a>
      <a href="#" style="left:864px">Contact</a>
    </nav>
    <div class="social" aria-label="Social links"><span></span><span></span><span></span></div>
  </footer>
</body>
</html>
```